Business Card Design Project

I need a cool business card design for the company that will build residential houses.
The card should include:
1) Name: Borek Valdisov
2) Cell: 587.244.XXXX
3) Email: bor.valdisov@qorvina.example
4) Position: General Manager
5) Residential Home Building
6) Company logo that I have uploaded

Industry/Entity Type

Residential

```html
<!DOCTYPE html>
<html lang="en">
<head>
<meta charset="utf-8">
<title>Qorvina Developments – Business Card</title>
<link rel="stylesheet" href="https://fonts.googleapis.com/css2?family=Open+Sans:wght@400;600;700&display=swap">
<style>
  :root {
    --backdrop: #070808;
    --card: #ffffff;
    --ink: #111111;
    --accent-green: #7fe21f;
    --accent-blue: #2a6fe6;
  }
  * { margin: 0; padding: 0; box-sizing: border-box; }
  html, body {
    width: 1200px; height: 846px; overflow: hidden;
    background: var(--backdrop);
    font-family: "Open Sans", Arial, sans-serif;
  }
  .card {
    position: absolute; left: 158px; top: 158px;
    width: 884px; height: 530px;
    background: var(--card);
  }
  .contact-group {
    position: absolute; left: 42px;
    padding-left: 41px;
    color: var(--ink);
    font-size: 22px; line-height: 28px;
  }
  .contact-group::before {
    content: ""; position: absolute; left: 0; top: 0;
    width: 8px; height: 124px; background: var(--accent-green);
  }
  .contact-group .icon { display: block; fill: var(--accent-blue); margin-bottom: 6px; }
  .group-address { top: 54px; padding-top: 18px; }
  .group-phone { top: 210px; padding-top: 18px; }
  .group-web { top: 369px; padding-top: 24px; }
  .brand-name {
    position: absolute; left: 420px; top: 240px; width: 420px;
    text-align: center;
    font-size: 44px; font-weight: 600; line-height: 1;
    color: var(--accent-blue);
  }
  .holder {
    position: absolute; right: 49px; top: 376px;
    padding-right: 12px; text-align: right; color: var(--ink);
  }
  .holder::after {
    content: ""; position: absolute; right: -20px; top: 0;
    width: 8px; height: 76px; background: var(--accent-green);
  }
  .holder-name { font-size: 31px; font-weight: 700; line-height: 42px; }
  .holder-title { font-size: 22px; line-height: 30px; }
</style>
</head>
<body>
  <div class="card">
    <div class="contact-group group-address">
      <svg class="icon" width="20" height="26" viewBox="0 0 20 26" aria-hidden="true">
        <path d="M10 0C4.5 0 0 4.3 0 9.7 0 16.8 10 26 10 26s10-9.2 10-16.3C20 4.3 15.5 0 10 0zm0 13a3.4 3.4 0 1 1 0-6.8 3.4 3.4 0 0 1 0 6.8z"/>
      </svg>
      <p>Residential Home Building</p>
      <p>Your Address</p>
      <p>10101</p>
    </div>

    <div class="contact-group group-phone">
      <svg class="icon" width="16" height="26" viewBox="0 0 16 26" aria-hidden="true">
        <path d="M3 0h10a3 3 0 0 1 3 3v20a3 3 0 0 1-3 3H3a3 3 0 0 1-3-3V3a3 3 0 0 1 3-3zm-1 4v16h12V4zm6 17.5a1.5 1.5 0 1 0 0 3 1.5 1.5 0 0 0 0-3z"/>
      </svg>
      <p>(office) - (1) 587.244.XXXX</p>
      <p>(mobile) - (1) 587.244.XXXX</p>
    </div>

    <div class="contact-group group-web">
      <svg class="icon" width="26" height="18" viewBox="0 0 26 18" aria-hidden="true">
        <path d="M0 0h26v18H0zM2 2.5v.6l11 8 11-8v-.6zm0 3.2V16h22V5.7l-11 8z"/>
      </svg>
      <p>bor.valdisov@qorvina.example</p>
      <p>www.xxxxx.xxx.com</p>
    </div>

    <p class="brand-name">Qorvina Developments</p>

    <div class="holder">
      <p class="holder-name">Borek Valdisov</p>
      <p class="holder-title">General Manager</p>
    </div>
  </div>
</body>
</html>
```